Banner Ad Design job - Bramblet Mortgage - Banner Ads for Re-Marketing Campaigns

Need a banner ad for a retargeting Campaign with Velvet Reach.

We would like to incorporate our attached logo. Also would like to incorporate a call to action "Pre-Qualify for a home loan today" and a button to click. This banner is to encourage previous customers to come back to our website and submit information. It must look good on mobile and desktop.

Our website is BrambletMortgage.example

Target Market(s)

Customers Seeking a Mortgage Loan

Industry/Entity Type

Mortgage Lender

Colors

Designer to choose colors to be used in the design.

Requirements
Must have
• - We would like the same basic design in the 4 sizes below.
• - 728x90 pixels leader board
• - 300x250 medium rectangle
• - 300x600 half page
• - 600x315 chatterbook
Nice to have
• Call to action. Click button or Something to promote them to click through
Should not have
• We are Open

```html
<!DOCTYPE html>
<html lang="en">
<head>
<meta charset="utf-8">
<title>Bramblet Mortgage – Pre-Qualify Banner</title>
<link rel="stylesheet" href="https://fonts.googleapis.com/css2?family=Open+Sans:wght@600;700&display=swap">
<style>
  :root {
    --brand-blue: #1f5fa8;
    --brand-sky: #f2b134;
    --panel-white: #ffffff;
    --cta-orange: #f6a01a;
    --cta-orange-dark: #e48d0c;
    --headline-white: #ffffff;
    --scene-sky: #8d8c86;
    --scene-hill: #4e4a43;
    --scene-sand: #7d7063;
    --scene-sea: #8c9aa6;
  }
  html, body {
    margin: 0;
    padding: 0;
    width: 1200px;
    height: 630px;
    overflow: hidden;
    background: #ffffff;
  }
  .banner {
    position: relative;
    width: 1200px;
    height: 630px;
    overflow: hidden;
    font-family: "Open Sans", Arial, sans-serif;
  }
  .beach-scene {
    position: absolute;
    inset: 0;
    background:
      linear-gradient(180deg, rgba(0,0,0,0.15) 0%, rgba(0,0,0,0.05) 45%, rgba(0,0,0,0.25) 100%),
      radial-gradient(ellipse 55% 45% at 88% 80%, var(--scene-sea) 0%, rgba(140,154,166,0) 70%),
      linear-gradient(172deg, var(--scene-sky) 0%, #6c6a63 18%, var(--scene-hill) 38%, #6a6156 55%, var(--scene-sand) 72%, #5f564c 100%);
  }
  .logo-panel {
    position: absolute;
    top: 0;
    left: 0;
    width: 620px;
    height: 196px;
  }
  .logo-panel svg { display: block; }
  .logo {
    position: absolute;
    top: 0;
    left: 34px;
    height: 196px;
    display: flex;
    align-items: center;
    gap: 20px;
  }
  .logo-dot {
    width: 64px;
    height: 64px;
    border-radius: 50%;
    background: var(--brand-blue);
    flex: none;
  }
  .logo-name {
    font-weight: 700;
    font-size: 46px;
    line-height: 1;
    color: var(--brand-blue);
    white-space: nowrap;
  }
  .headline {
    position: absolute;
    left: 28px;
    top: 222px;
    margin: 0;
    font-weight: 600;
    font-size: 96px;
    line-height: 104px;
    color: var(--headline-white);
    letter-spacing: -0.5px;
    text-shadow: 0 2px 6px rgba(0,0,0,0.25);
  }
  .cta-button {
    position: absolute;
    left: 30px;
    top: 474px;
    width: 490px;
    height: 120px;
    border-radius: 8px;
    background: linear-gradient(180deg, var(--cta-orange) 0%, var(--cta-orange-dark) 100%);
    color: #ffffff;
    font-weight: 600;
    font-size: 62px;
    display: flex;
    align-items: center;
    justify-content: center;
    text-decoration: none;
  }
</style>
</head>
<body>
  <div class="banner">
    <div class="beach-scene" role="img" aria-label="Photo of a sandy beach at dusk with waves on the right and hillside houses and palm trees behind"></div>

    <div class="logo-panel">
      <svg width="620" height="196" viewBox="0 0 620 196" aria-hidden="true">
        <polygon points="0,0 620,0 570,196 0,196" fill="var(--panel-white)"/>
      </svg>
      <div class="logo">
        <span class="logo-dot"></span>
        <span class="logo-name">Bramblet Mortgage</span>
      </div>
    </div>

    <h1 class="headline">Pre-Qualify<br>for a Home loan today</h1>

    <a class="cta-button" href="#">Apply Online</a>
  </div>
</body>
</html>
```